Electronic Law Reports publisher needs App Design (Design Only / 8 screens)

We need app designs for a complete rewrite of our Electronic Legal Research Software - CaseHarbor (http://caseharbor-demo.net).

We're looking to release a new version (which is aimed specifically at being a tool for Legal Research) on the PC and Android and we're very much interested in aligning our applications' look and feel with the current trends on these platforms while recreating the experience of using a Law Library.

Our application is an extensive Law Library. We provide in-depth analysis of Judgments delivered in Nigeria's Appellate Courts as well as other law related content aimed at helping lawyers, judges and legal practitioners enhance their practice.

The primary objective of this release for us is to be a replacement for Law Reports printed on paper and to recreate the experience of working with books within the context of a library.

We've described a number of use cases in the PDF file attached to this brief. There are about 8 different use-cases, meaning 8 screens.

Some of the features of our application include lists of Supreme Court Judgments, Court of Appeal Judgments, The Latest Judgments from both Courts, The Laws of the Federation, The Rules of Courts, Civil Procedure Rules, etc.

We're planning to present judgments in a view that's very similar to books i.e. Users would be able to take notes, highlight text and do other things in almost the same way they do on paper.

We think it's also important to note that majority of our customers are not as technologically savvy as the rest of us so the interfaces should be uncluttered with more focus on content.

The online version of our application is hosted at: http://caseharborplus-demo.net

Our App on TuneMarket: https://apps.example-store.net/ng/app/caseharbor-plus-pro/id804615293

While designers are free to make their decisions regarding color palettes, we would however like to see designs that are "skinnable" (Allow end-users to change color schemes)

Again, it is important that the primary user experience is one of using the Library. We'd also advice that designers checkout our iOS app and the Online version to get a better grip on our range of features.

Please see detailed description in the attached PDF file.

Initially, the screens we would love to see are:

* Home screen,
* Search results screen,
* Judgment Reading screen and
* a view of the user's research folder.

If you were unable to submit your designs before the deadline you can send us a message and if we get at least 5 designers, we'd consider extending the project.

Target Market(s)

Lawyers, Judges, Solicitors, General Legal Practitioners and Law Students

Industry/Entity Type

Electronic

Font styles to use
Serif
Other font styles liked:
• Roboto, Open Sans

Requirements
Must have
• The primary objective is to recreate the experience of using the Library. We're are striving to become a direct replacement for books in the Legal profession and the designs must support this sentiment.
• Judgments being read must be presented in a book view!
Nice to have
• While we're yet to come up with a name for this product, designers can create product names and logos as they see fit.
• We've seen good things about Zenoq's Fabric Layout for the Android platform.
• We wouldn't have a problem using a similar approach for our Desktop solution too.
Should not have
• Attached Images must only be used as reference guides to get an idea of what our current products do and look like.

```html
<!DOCTYPE html>
<html lang="en">
<head>
<meta charset="utf-8">
<title>CaseHarbor – Law Reports</title>
<link href="https://fonts.googleapis.com/css2?family=Tinos:wght@400;700&family=Roboto:wght@400;500;700&display=swap" rel="stylesheet">
<style>
  :root{
    --bg:#ffffff;
    --bar:#4e4a47;
    --bar-icon:#dcd8d4;
    --gray:#5b5757;
    --pink:#cc5c7a;
    --green:#3f8c66;
    --orange:#f5855a;
    --mint:#9ed69b;
    --ink:#555;
    --blue:#2f6fc0;
    --wood:#8b5b33;
    --wood-dark:#5e3b20;
    --shelf-back:#3b2a1e;
    --book:#2f3a68;
    --book-edge:#252e55;
    --book-label:#f1e3c3;
    --page:#fbfbfa;
    --case-red:#b0475a;
  }
  *{margin:0;padding:0;box-sizing:border-box}
  html,body{width:900px;height:1200px;overflow:hidden;background:var(--bg)}
  body{position:relative;font-family:"Tinos",serif}

  .app-header{position:absolute;left:77px;top:103px;width:768px;height:73px;background:var(--bar)}
  .brand{position:absolute;left:21px;top:12px;display:flex;align-items:center;gap:10px}
  .brand-mark{width:54px;height:54px;border:2px solid #e9e6e3;border-radius:50%}
  .brand-name{font-family:"Roboto",sans-serif;font-weight:500;font-size:27px;color:#efece9;line-height:1}
  .brand-tagline{position:absolute;left:86px;top:51px;font-family:"Roboto",sans-serif;font-size:9.5px;color:#e9e6e3;white-space:nowrap}
  .search-icon{position:absolute;right:30px;top:24px}

  .nav-tiles{position:absolute;left:77px;top:176px;width:768px;height:287px;display:flex}
  .nav-tiles span{height:100%;border-left:3px solid rgba(255,255,255,.35)}
  .nav-tiles span:first-child{border-left:0}
  .band-dark{position:absolute;left:77px;top:232px;width:768px;height:130px;background:rgba(40,30,30,.13)}
  .band-light{position:absolute;left:77px;top:362px;width:768px;height:101px;background:rgba(255,255,255,.78);border-bottom:1px solid #ddd}

  .menu-icon{position:absolute;left:86px;top:193px}
  .recent-tag{position:absolute;left:125px;top:188px;height:30px;width:110px;background:var(--pink);
    clip-path:polygon(0 0,92% 0,100% 50%,92% 100%,0 100%);color:#fff;font-size:21px;padding-left:23px;line-height:30px;
    box-shadow:0 0 0 1px rgba(255,255,255,.3)}

  .nav-item{position:absolute;top:262px;color:#fff;text-align:center;transform:translateX(-50%);line-height:1.05}
  .nav-item .lead{display:block;font-size:25px}
  .nav-item .rest{display:block;font-size:19px;line-height:1.25}

  .section-title{position:absolute;left:332px;top:400px;display:flex;align-items:center;gap:20px;color:var(--ink);font-size:29px}

  .court-tabs{position:absolute;left:77px;top:463px;width:768px;height:57px}
  .court-tab{position:absolute;top:20px;font-size:18px;text-transform:uppercase;transform:translateX(-50%);white-space:nowrap}
  .court-tab.active{left:203px;color:var(--blue)}
  .court-tab.idle{left:575px;color:#4a4a4a}
  .court-tabs .divider{position:absolute;left:384px;top:0;width:1px;height:57px;background:#ccc}

  .volume{position:absolute;left:24px;top:505px;width:873px;height:510px;background:#f6f6f6;box-shadow:0 3px 10px rgba(0,0,0,.18)}
  .volume .inner{position:absolute;left:42px;top:8px;width:780px;height:494px;background:#fff}
  .volume .spine-top,.volume .spine-bottom{position:absolute;left:231px;width:412px;height:8px;background:#a8b8c6}
  .volume .spine-top{top:0}.volume .spine-bottom{bottom:0}
  .ribbon{position:absolute;left:400px;top:1010px;width:12px;height:35px;background:#e6b0a6;clip-path:polygon(0 0,100% 0,100% 100%,50% 85%,0 100%)}

  .bookcase{position:absolute;left:52px;top:538px;width:816px;height:441px;background:var(--wood);
    border:2px solid var(--wood-dark);box-shadow:0 2px 6px rgba(0,0,0,.3)}
  .shelf-row{position:absolute;left:12px;width:788px;height:132px;background:var(--shelf-back);display:flex;gap:11px;padding:12px 0 0 10px}
  .shelf-row.r1{top:8px}.shelf-row.r2{top:150px}.shelf-row.r3{top:294px}
  .report{width:86px;height:118px;background:linear-gradient(90deg,var(--book-edge),var(--book) 10%,var(--book) 90%,var(--book-edge));
    text-align:center;padding-top:20px;box-shadow:inset 0 0 0 1px rgba(255,255,255,.05)}
  .report .series{font-size:12.5px;color:var(--book-label);line-height:1.1;text-transform:uppercase}
  .report .case{font-family:"Roboto",sans-serif;font-size:13.5px;color:#f3f3f6;margin-top:16px;line-height:1.5}
  .report .case.three{margin-top:6px}

  .open-report{position:absolute;left:172px;top:548px;width:326px;height:234px;background:var(--book);border-radius:3px;box-shadow:0 6px 14px rgba(0,0,0,.45)}
  .open-report .page{position:absolute;top:4px;height:224px;background:var(--page)}
  .open-report .left{left:8px;width:155px;border-right:1px solid #ddd;background:linear-gradient(90deg,#fff 80%,#e9e9e9)}
  .open-report .right{left:163px;width:155px;background:linear-gradient(90deg,#e7e7e7,#fff 18%)}
  .case-title{position:absolute;left:11px;top:33px;font-family:"Roboto",sans-serif;font-size:14px;color:#3c4660;white-space:nowrap}
  .case-date{position:absolute;left:11px;top:52px;font-family:"Roboto",sans-serif;font-size:14px;color:var(--case-red);white-space:nowrap}
  .case-number{position:absolute;left:24px;top:133px;font-family:"Roboto",sans-serif;font-size:16px;color:var(--blue)}
  .pointer{position:absolute;left:34px;top:86px}
  .crest{position:absolute;left:69px;top:6px;width:16px;height:16px;border-radius:50%;background:#8fb58f}
  .fine{position:absolute;left:0;width:100%;font-family:"Roboto",sans-serif;font-size:4px;color:#666;text-align:center;line-height:1.5}
  .bench{position:absolute;left:6px;width:143px;font-family:"Roboto",sans-serif;font-size:4px;color:#777;line-height:8px}
  .bench div{display:flex;justify-content:space-between;border-bottom:1px dotted #bbb}

  .toolbar{position:absolute;left:77px;top:1056px;width:768px;height:70px;background:var(--bar)}
  .toolbar svg{position:absolute;top:22px}
</style>
</head>
<body>

<header class="app-header">
  <div class="brand"><span class="brand-mark"></span><span class="brand-name">CaseHarbor</span></div>
  <div class="brand-tagline">Electronic Legal Research Software 7.0</div>
  <svg class="search-icon" width="30" height="30" viewBox="0 0 30 30" fill="none" stroke="#e5e2df" stroke-width="3"><circle cx="12" cy="12" r="8"/><path d="M18 18l9 9" stroke-linecap="round"/></svg>
</header>

<div class="nav-tiles">
  <span style="width:47px;background:var(--gray)"></span>
  <span style="width:177px;background:var(--pink)"></span>
  <span style="width:124px;background:var(--green)"></span>
  <span style="width:126px;background:var(--gray)"></span>
  <span style="width:133px;background:var(--orange)"></span>
  <span style="width:161px;background:var(--green)"></span>
</div>
<div class="band-dark"></div>
<div class="band-light"></div>

<svg class="menu-icon" width="28" height="20" viewBox="0 0 28 20" fill="#fff"><rect y="0" width="28" height="3"/><rect y="8.5" width="28" height="3"/><rect y="17" width="28" height="3"/></svg>
<div class="recent-tag">Recent</div>

<nav>
  <div class="nav-item" style="left:240px"><span class="lead">All</span><span class="rest">Judgments</span></div>
  <div class="nav-item" style="left:361px"><span class="lead">My</span><span class="rest">Library</span></div>
  <div class="nav-item" style="left:488px"><span class="lead">My</span><span class="rest">Research<br>Folder</span></div>
  <div class="nav-item" style="left:613px"><span class="lead">Laws</span><span class="rest">of the<br>Federation</span></div>
  <div class="nav-item" style="left:754px"><span class="lead">Civil</span><span class="rest">Procedure<br>Rules</span></div>
</nav>

<div class="section-title">
  <svg width="34" height="30" viewBox="0 0 34 30" fill="#555"><rect x="10" y="2" width="16" height="8" rx="1" transform="rotate(-35 18 6)"/><rect x="17" y="8" width="4" height="14" transform="rotate(-35 19 15)"/><rect x="2" y="23" width="24" height="5" rx="1"/></svg>
  <span>Law Reports</span>
</div>

<div class="court-tabs">
  <span class="court-tab active">Supreme Court</span>
  <span class="divider"></span>
  <span class="court-tab idle">Court of Appeal</span>
</div>

<div class="volume"><div class="inner"></div><div class="spine-top"></div><div class="spine-bottom"></div></div>
<div class="ribbon"></div>

<section class="bookcase">
  <div class="shelf-row r1">
    <div class="report"><div class="series">Law<br>Reports</div><div class="case">JONAS v.<br>IDEC &amp; ORS</div></div>
    <div class="report"><div class="series">Law<br>Reports</div><div class="case">ADEVO v.<br>STATE</div></div>
    <div class="report"><div class="series">Law<br>Reports</div><div class="case three">KEMBA v.<br>OLUFARI-<br>NDE &amp; ORS</div></div>
    <div class="report"><div class="series">Law<br>Reports</div><div class="case">JONAS v.<br>IDEC &amp; ORS</div></div>
    <div class="report"><div class="series">Law<br>Reports</div><div class="case">ADEVO v.<br>STATE</div></div>
    <div class="report"><div class="series">Law<br>Reports</div><div class="case three">KEMBA v.<br>OLUFARI-<br>NDE &amp; ORS</div></div>
    <div class="report"><div class="series">Law<br>Reports</div><div class="case">JONAS v.<br>IDEC &amp; ORS</div></div>
    <div class="report"><div class="series">Law<br>Reports</div><div class="case">ADEVO v.<br>STATE</div></div>
  </div>
  <div class="shelf-row r2">
    <div class="report"><div class="series">Law<br>Reports</div><div class="case">JONAS v.<br>IDEC &amp; ORS</div></div>
    <div class="report"><div class="series">Law<br>Reports</div><div class="case">ADEVO v.<br>STATE</div></div>
    <div class="report"><div class="series">Law<br>Reports</div><div class="case three">KEMBA v.<br>OLUFARI-<br>NDE &amp; ORS</div></div>
    <div class="report"><div class="series">Law<br>Reports</div><div class="case">JONAS v.<br>IDEC &amp; ORS</div></div>
    <div class="report"><div class="series">Law<br>Reports</div><div class="case">ADEVO v.<br>STATE</div></div>
    <div class="report"><div class="series">Law<br>Reports</div><div class="case three">KEMBA v.<br>OLUFARI-<br>NDE &amp; ORS</div></div>
    <div class="report"><div class="series">Law<br>Reports</div><div class="case">JONAS v.<br>IDEC &amp; ORS</div></div>
    <div class="report"><div class="series">Law<br>Reports</div><div class="case">ADEVO v.<br>STATE</div></div>
  </div>
  <div class="shelf-row r3">
    <div class="report"><div class="series">Law<br>Reports</div><div class="case">JONAS v.<br>IDEC &amp; ORS</div></div>
    <div class="report"><div class="series">Law<br>Reports</div><div class="case">ADEVO v.<br>STATE</div></div>
    <div class="report"><div class="series">Law<br>Reports</div><div class="case three">KEMBA v.<br>OLUFARI-<br>NDE &amp; ORS</div></div>
    <div class="report"><div class="series">Law<br>Reports</div><div class="case">JONAS v.<br>IDEC &amp; ORS</div></div>
    <div class="report"><div class="series">Law<br>Reports</div><div class="case">ADEVO v.<br>STATE</div></div>
    <div class="report"><div class="series">Law<br>Reports</div><div class="case three">KEMBA v.<br>OLUFARI-<br>NDE &amp; ORS</div></div>
    <div class="report"><div class="series">Law<br>Reports</div><div class="case">JONAS v.<br>IDEC &amp; ORS</div></div>
    <div class="report"><div class="series">Law<br>Reports</div><div class="case">ADEVO v.<br>STATE</div></div>
  </div>
</section>

<article class="open-report">
  <div class="page left">
    <div class="case-title">JONAS v. IDEC &amp; ORS</div>
    <div class="case-date">(On 13th March,2015)</div>
    <svg class="pointer" width="20" height="26" viewBox="0 0 20 26" fill="#fff" stroke="#333" stroke-width="1.2"><path d="M6 2c1.2 0 2 .8 2 2v8l1-.2V9.5c0-1 1.8-1 2 0v2.3l1 .1v-1.6c0-1 1.8-1 2 0v2l1 .2v-1c0-1 1.8-1 1.8 0V18c0 4-2.5 6.5-6 6.5S5 22.5 3.5 19L1.5 14c-.4-1 .8-1.8 1.6-1L4 14.5V4c0-1.2.8-2 2-2z"/></svg>
    <div class="case-number">SC.478/2013</div>
  </div>
  <div class="page right">
    <div class="crest" role="img" aria-label="Court crest emblem"></div>
    <div class="fine" style="top:24px">In the Supreme Court<br>Friday 13th March 2015<br><span style="color:var(--case-red)">SC.478/2013</span></div>
    <div class="fine" style="top:50px;font-weight:500">Before Their Lordships</div>
    <div class="bench" style="top:58px">
      <div><span>A. K. Dele, JSC</span><span>Justice, Supreme Court</span></div>
      <div><span>M. O. Bade, JSC</span><span>Justice, Supreme Court</span></div>
      <div><span>S. T. Iro, JSC</span><span>Justice, Supreme Court</span></div>
      <div><span>F. N. Oke, JSC</span><span>Justice, Supreme Court</span></div>
      <div><span>R. A. Udo, JSC</span><span>Justice, Supreme Court</span></div>
    </div>
    <div class="fine" style="top:104px;font-weight:500">Between</div>
    <div class="fine" style="top:112px">1. Jonas Dede<br>2. Tayo Ranti<br>3. Ngozi Fela<br>and<br>1. Idec Board<br>2. Sade Obi<br>3. Kunle Eze<br>4. Bisi Ola<br>5. Chidi Ume<br>6. Remi Ade</div>
  </div>
</article>

<footer class="toolbar">
  <svg style="left:66px" width="24" height="24" viewBox="0 0 24 24" fill="none" stroke="var(--bar-icon)" stroke-width="3" stroke-linecap="round" stroke-linejoin="round"><path d="M7 4L3 8l4 4"/><path d="M3 8h11a6 6 0 0 1 0 12H9"/></svg>
  <svg style="left:186px" width="30" height="26" viewBox="0 0 30 26" fill="none" stroke="var(--bar-icon)" stroke-width="3" stroke-linejoin="round"><path d="M9 3H3v20h24V3h-6"/><path d="M15 2v13M10 10l5 5 5-5" stroke-linecap="round"/></svg>
  <svg style="left:309px" width="28" height="28" viewBox="0 0 28 28" fill="none" stroke="var(--bar-icon)" stroke-width="3"><circle cx="14" cy="14" r="8"/><path d="M14 1v5M14 22v5M1 14h5M22 14h5M4.8 4.8l3.5 3.5M19.7 19.7l3.5 3.5M4.8 23.2l3.5-3.5M19.7 8.3l3.5-3.5"/></svg>
  <svg style="left:432px" width="46" height="28" viewBox="0 0 46 28" fill="var(--bar-icon)"><path d="M0 2h32v18H0z M4 5v12h24V5z"/><circle cx="16" cy="11" r="4"/><rect x="4" y="22" width="28" height="2.5"/><ellipse cx="38" cy="14" rx="7" ry="2.5"/><ellipse cx="38" cy="19" rx="7" ry="2.5"/><ellipse cx="38" cy="24" rx="7" ry="2.5"/></svg>
  <svg style="left:560px" width="26" height="28" viewBox="0 0 26 28" fill="none" stroke="var(--bar-icon)" stroke-width="3" stroke-linecap="round" stroke-linejoin="round"><path d="M4 12a9 9 0 0 1 15-6l2 2"/><path d="M21 3v5h-5"/><path d="M22 16a9 9 0 0 1-15 6l-2-2"/><path d="M5 25v-5h5"/></svg>
  <svg style="left:673px" width="24" height="28" viewBox="0 0 24 28" fill="var(--bar-icon)"><path d="M12 1L2 5v8c0 7 4.5 11.5 10 14 5.5-2.5 10-7 10-14V5z"/><path d="M7 14l4 4 7-8" fill="none" stroke="var(--bar)" stroke-width="3" stroke-linecap="round" stroke-linejoin="round"/></svg>
</footer>

</body>
</html>
```